Book Cover Design for first time business owners

Looking for a design for my book, 'LAYING THE GROUNDWORK' subtitle is
THE SITE, LEASING, PLANNING, & BUILD-OUT STAGES FOR LAUNCHING YOUR SHOP OR CAFÉ VENTURE ON SCHEDULE AND WITHIN COST

If it helps, below is part of the preface:

These pages derive from my experiences and industry standards. This book runs through the budgeting, real estate, design, construction, signage, and equipment processes needed to get any retail or restaurant space open on-time and on budget while saving you time, money, and headaches along the way.

Whether it be a one-off enterprise or franchise, flower shop, or swim center; the steps and procedures are strikingly similar. Whether you’re looking to spend $200,000 or $2,000,000, it’s all largely the same.
This book does not discuss marketing or operations as those items are more concept specific, and outside the confines of this book.
Technically food-service concepts (restaurants, cafés, and bars) are not considered retail. For the basis of this book and to streamline writing, mentions of retail include food-service concepts.

Target Market(s)

First time business Owners looking to construct a retail or food-service concept

Font styles to use
Serif

Requirements
Must have
• I'm open to any designs! Looking for the design to wrap around the front, spine, and back.
• Please include the authors name on the front: Corwin Halbeck. The Authors name size should not be overly intrusive.
• I'm still working on the verbiage for the back of the book. That verbiage will be on the top half of the back.

```html
<!DOCTYPE html>
<html lang="en">
<head>
<meta charset="utf-8">
<title>Laying the Groundwork — Book Cover</title>
<link href="https://fonts.googleapis.com/css2?family=Libre+Baskerville:wght@400;700&family=Tinos:wght@400;700&display=swap" rel="stylesheet">
<style>
  :root {
    --stage-bg: #e9e7e4;
    --cover-white: #fbfcfd;
    --navy: #1f2a6e;
    --teal: #2ea6c8;
    --band-navy: #1d2a74;
    --band-text: #43b8d8;
    --photo-light: #f4f5f7;
    --photo-mid: #d9dbe0;
  }
  * { box-sizing: border-box; margin: 0; padding: 0; }
  html, body {
    width: 1200px;
    height: 800px;
    overflow: hidden;
    background: var(--stage-bg);
  }
  .stage {
    position: relative;
    width: 1200px;
    height: 800px;
  }
  .book-cover {
    position: absolute;
    left: 350px;
    top: 20px;
    width: 500px;
    height: 760px;
    background: var(--cover-white);
    box-shadow: 0 6px 24px rgba(0,0,0,0.18);
    overflow: hidden;
  }
  .cover-photo {
    position: absolute;
    left: 0;
    top: 0;
    width: 500px;
    height: 400px;
    background:
      radial-gradient(ellipse 55% 45% at 50% 42%, rgba(184,138,108,0.55), rgba(110,74,54,0.18) 55%, rgba(255,255,255,0) 80%),
      linear-gradient(180deg, var(--photo-light) 0%, var(--photo-mid) 45%, var(--photo-light) 80%, var(--cover-white) 100%);
  }
  .cover-photo::after {
    content: "";
    position: absolute;
    left: 0; right: 0; bottom: 0;
    height: 120px;
    background: linear-gradient(180deg, rgba(251,252,253,0) 0%, var(--cover-white) 100%);
  }
  .title-block {
    position: absolute;
    left: 0;
    top: 372px;
    width: 500px;
    text-align: center;
  }
  .book-title {
    font-size: inherit;
    font-weight: 400;
  }
  .title-line-top {
    display: block;
    font-family: "Libre Baskerville", "Tinos", serif;
    font-weight: 700;
    font-size: 62px;
    line-height: 1;
    color: var(--navy);
  }
  .title-connector {
    display: flex;
    align-items: center;
    justify-content: center;
    gap: 10px;
    margin-top: 6px;
    height: 42px;
  }
  .title-connector .word {
    font-family: "Tinos", serif;
    font-weight: 400;
    font-size: 38px;
    line-height: 1;
    color: var(--navy);
  }
  .title-connector svg { display: block; }
  .title-line-main {
    display: block;
    font-family: "Libre Baskerville", "Tinos", serif;
    font-weight: 700;
    font-size: 48px;
    line-height: 1;
    color: var(--teal);
    margin-top: 10px;
    letter-spacing: -0.5px;
  }
  .title-rule {
    display: block;
    margin: 20px auto 0;
  }
  .subtitle {
    margin: 7px auto 0;
    width: 460px;
    font-family: "Tinos", serif;
    font-size: 17px;
    line-height: 16px;
    color: var(--teal);
    text-align: center;
    text-transform: uppercase;
  }
  .subtitle-rule {
    display: block;
    margin: 4px auto 0;
  }
  .author-band {
    position: absolute;
    left: 0;
    bottom: 0;
    width: 500px;
    height: 60px;
    background: var(--band-navy);
    border-top: 3px solid var(--cover-white);
    box-shadow: 0 -2px 0 var(--band-navy);
    display: flex;
    align-items: center;
    justify-content: center;
  }
  .author-name {
    font-family: "Tinos", serif;
    font-size: 30px;
    letter-spacing: 5px;
    color: var(--band-text);
    text-transform: uppercase;
  }
</style>
</head>
<body>
  <main class="stage">
    <section class="book-cover">
      <div class="cover-photo" role="img" aria-label="Photograph of several business people's hands clasping one another's wrists in a connected circle, seen from above against white"></div>

      <div class="title-block">
        <h1 class="book-title">
          <span class="title-line-top">LAYING</span>
          <span class="title-connector">
            <svg width="82" height="18" viewBox="0 0 82 18" aria-hidden="true">
              <g stroke="var(--teal)" stroke-width="1.5">
                <line x1="0" y1="3" x2="82" y2="3"/>
                <line x1="0" y1="9" x2="82" y2="9"/>
                <line x1="0" y1="15" x2="82" y2="15"/>
              </g>
            </svg>
            <span class="word">THE</span>
            <svg width="82" height="18" viewBox="0 0 82 18" aria-hidden="true">
              <g stroke="var(--teal)" stroke-width="1.5">
                <line x1="0" y1="3" x2="82" y2="3"/>
                <line x1="0" y1="9" x2="82" y2="9"/>
                <line x1="0" y1="15" x2="82" y2="15"/>
              </g>
            </svg>
          </span>
          <span class="title-line-main">GROUNDWORK</span>
        </h1>

        <svg class="title-rule" width="400" height="3" viewBox="0 0 400 3" aria-hidden="true">
          <line x1="0" y1="1.5" x2="400" y2="1.5" stroke="var(--navy)" stroke-width="2"/>
        </svg>

        <p class="subtitle">The Site, Leasing, Planning, &amp; Build-Out<br>Stages for Launching Your Shop or<br>Café Venture on Schedule<br>and Within Cost</p>

        <svg class="subtitle-rule" width="140" height="3" viewBox="0 0 140 3" aria-hidden="true">
          <line x1="0" y1="1.5" x2="140" y2="1.5" stroke="var(--navy)" stroke-width="1.5"/>
        </svg>
      </div>

      <div class="author-band">
        <p class="author-name">Corwin Halbeck</p>
      </div>
    </section>
  </main>
</body>
</html>
```